Christmas and New Year wishes

I would like to send as a picture in a email a graphic that relates to:
-thanks for the collaboration / partnership in the past year (to be used for customers and partners)
-Wishes for Merry christmas and a successful 2019
-it should be colored and possibly include our logo color (www.velkari.ch) (nice to have), or the name of our company

Target Market(s)

Customers and partners

Industry/Entity Type

It Company

Font styles to use
Sans Serif

Colors
9bcb3c
0455a3

Requirements
Must have
• Relation to christmas
• Relation to New year
Nice to have
• The colors below are near to the company logo color. But feel free to use any other logo
• a funny design
• Happy Customer or partner (supplier)
• Can be a mixture of text and drawing

```html
<!DOCTYPE html>
<html lang="en">
<head>
<meta charset="utf-8">
<title>Christmas and New Year Wishes – Velkari</title>
<link rel="stylesheet" href="https://fonts.googleapis.com/css2?family=Sacramento&family=EB+Garamond:wght@400&display=swap">
<style>
  :root {
    --paper: #ffffff;
    --green-deep: #03553a;
    --green-mid: #026a2c;
    --green-glow: #07791f;
    --lime: #b6e322;
    --brand-lime: #9bcb3c;
    --brand-blue: #0455a3;
    --ink-light: #ffffff;
  }
  * { margin: 0; padding: 0; box-sizing: border-box; }
  html, body {
    width: 1003px;
    height: 1200px;
    overflow: hidden;
    background: var(--paper);
  }
  .card {
    position: relative;
    width: 1003px;
    height: 1200px;
    background: var(--paper);
  }
  .card__panel {
    position: absolute;
    left: 36px;
    top: 0;
    width: 943px;
    height: 1194px;
    background: radial-gradient(ellipse 60% 50% at 50% 43%, var(--green-glow) 0%, var(--green-mid) 45%, var(--green-deep) 100%);
    overflow: hidden;
  }
  .snowfall {
    position: absolute;
    left: 20px;
    top: 20px;
    width: 900px;
    height: 640px;
    border-radius: 50%;
    background: radial-gradient(ellipse at 50% 50%, rgba(255,255,255,0.10) 0%, rgba(255,255,255,0.05) 50%, rgba(255,255,255,0) 72%);
  }
  .line {
    position: absolute;
    left: 0;
    width: 100%;
    text-align: center;
    color: var(--ink-light);
    white-space: nowrap;
  }
  .script { font-family: "Sacramento", cursive; font-weight: 400; }
  .serif { font-family: "EB Garamond", "Times New Roman", serif; font-weight: 400; }

  .headline-merry {
    top: 150px;
    left: 60px;
    font-size: 230px;
    line-height: 1;
  }
  .headline-christmas {
    top: 300px;
    left: 0;
    font-size: 250px;
    line-height: 1;
  }
  .addressee {
    top: 530px;
    font-size: 64px;
    line-height: 1;
    color: var(--lime);
  }
  .thanks {
    font-size: 33px;
    line-height: 1;
  }
  .thanks--first { top: 644px; }
  .thanks--second { top: 686px; }
  .wish-script {
    top: 722px;
    left: 14px;
    font-size: 62px;
    line-height: 1;
  }
  .wish-year {
    top: 774px;
    left: 14px;
    font-size: 44px;
    line-height: 1;
  }
  .wish-number {
    top: 828px;
    left: 14px;
    font-size: 100px;
    line-height: 1;
  }
  .signoff {
    top: 920px;
    left: 10px;
    font-size: 82px;
    line-height: 1;
  }
  .brand-name {
    top: 1010px;
    left: 10px;
    font-size: 46px;
    line-height: 1;
    color: var(--brand-lime);
    letter-spacing: 2px;
  }
</style>
</head>
<body>
  <main class="card">
    <section class="card__panel">
      <div class="snowfall" role="img" aria-label="Scattered white snow speckles around the greeting"></div>

      <h1 class="line script headline-merry">Merry</h1>
      <p class="line script headline-christmas">Christmas</p>
      <p class="line script addressee">to all clients</p>

      <p class="line serif thanks thanks--first">Thank you for the collaboration and partnership.</p>
      <p class="line serif thanks thanks--second">Thank you for another successful year. I want to wish you a</p>

      <p class="line script wish-script">Merry Christmas &amp;</p>
      <p class="line serif wish-year">a Successful year in</p>
      <p class="line serif wish-number">2019!</p>

      <p class="line script signoff">Love</p>
      <p class="line serif brand-name">Velkari</p>
    </section>
  </main>
</body>
</html>
```